Looking for something sharp classy and with an edge for an advanced civil construction business
Something that says professional
nothing too DARK

Target Market(s)

mining companies council civil contractors concrete works

Industry/Entity Type

Construction

Contact Information for Business Card

Ridgeline Civil Constructions
ridgelinecivilconstruction@mailtrove.net
Rewi Ashdown
0412758391

Font styles to use
Serif
Sans Serif

Colors
0455a3
0592cd
85cae6
000000
919191

Requirements
Must have
• On the back of the card must have
down the bottom small print email logo phone number

Should not have
• follow us on facebook
Ridgeline Civil Constructions

follow us on instagram
RIDGELINECIVILCONSTRUCTIONS

```html
<!DOCTYPE html>
<html lang="en">
<head>
<meta charset="utf-8">
<title>Ridgeline Civil Constructions – Business Card</title>
<link rel="stylesheet" href="https://fonts.googleapis.com/css2?family=Arimo:wght@400;700&display=swap">
<style>
  :root {
    --page-bg: #e9e9ea;
    --blue-deep: #2e2f8f;
    --blue-mid: #0455a3;
    --blue-bright: #0592cd;
    --blue-light: #85cae6;
    --ink: #000000;
    --steel: #d4d6da;
    --label-bg: #0c2d52;
    --white: #ffffff;
  }
  * { box-sizing: border-box; margin: 0; padding: 0; }
  html, body {
    width: 1200px; height: 1200px; overflow: hidden;
    background: var(--page-bg);
    font-family: "Arimo", Arial, sans-serif;
  }
  .canvas { position: relative; width: 1200px; height: 1200px; }
  .card {
    position: absolute; left: 140px; width: 920px; height: 560px;
    overflow: hidden;
    box-shadow: 0 4px 14px rgba(0,0,0,0.25);
  }
  .card--front {
    top: 30px;
    background: radial-gradient(ellipse 60% 70% at 50% 40%, var(--blue-bright) 0%, #1f6bbb 45%, var(--blue-deep) 100%);
  }
  .brand-lockup {
    position: absolute; left: 0; right: 0; top: 215px;
    text-align: center;
  }
  .brand-lockup__name {
    font-weight: 700; font-size: 76px; letter-spacing: 6px;
    color: var(--steel); line-height: 1;
  }
  .brand-lockup__tagline {
    margin-top: 12px;
    font-weight: 700; font-size: 33px; letter-spacing: 1px;
    color: #151a2e;
  }
  .card--back { top: 610px; background: var(--blue-mid); }
  .back-texture {
    position: absolute; inset: 0;
    background: radial-gradient(ellipse 70% 80% at 50% 45%, #3a9ad6 0%, #2478c0 55%, #1c5fa9 100%);
  }
  .name-label {
    position: absolute; left: 48px; top: 78px;
    padding: 8px 16px 10px;
    background: var(--label-bg);
    color: var(--white); font-weight: 700; font-size: 34px;
  }
  .social-links {
    position: absolute; right: 52px; top: 78px;
    display: flex; gap: 14px;
  }
  .social-links__tile {
    width: 58px; height: 58px; border-radius: 8px;
    background: linear-gradient(#f4f8fc, #c9dcee);
  }
  .contact-list {
    position: absolute; left: 50px; bottom: 38px;
    list-style: none; color: var(--white); font-size: 23px;
  }
  .contact-list__item { display: flex; align-items: center; gap: 12px; height: 38px; }
  .contact-list__icon {
    width: 24px; height: 24px; background: var(--white);
    display: flex; align-items: center; justify-content: center;
    color: var(--blue-mid); font-size: 18px; font-weight: 700;
  }
  .back-brand {
    position: absolute; right: 40px; bottom: 42px;
    color: var(--white); font-weight: 700; font-size: 50px; letter-spacing: 3px;
  }
</style>
</head>
<body>
<main class="canvas">
  <section class="card card--front" aria-label="Card front">
    <div class="brand-lockup">
      <div class="brand-lockup__name">RIDGELINE</div>
      <div class="brand-lockup__tagline">CIVIL CONSTRUCTIONS</div>
    </div>
  </section>

  <section class="card card--back" aria-label="Card back">
    <div class="back-texture" role="img" aria-label="Blue background with a faint repeating brand-name pattern"></div>
    <div class="name-label">Rewi Ashdown</div>
    <div class="social-links" aria-label="Social media">
      <span class="social-links__tile" role="img" aria-label="Photo-sharing profile"></span>
      <span class="social-links__tile" role="img" aria-label="Social network page"></span>
    </div>
    <ul class="contact-list">
      <li class="contact-list__item">
        <span class="contact-list__icon">@</span>
        <span>ridgelinecivilconstruction@mailtrove.net</span>
      </li>
      <li class="contact-list__item">
        <span class="contact-list__icon">
          <svg width="18" height="18" viewBox="0 0 24 24" aria-hidden="true">
            <path fill="#0455a3" d="M6.6 10.8a15.1 15.1 0 0 0 6.6 6.6l2.2-2.2a1 1 0 0 1 1-.25 11.4 11.4 0 0 0 3.6.57 1 1 0 0 1 1 1V20a1 1 0 0 1-1 1A17 17 0 0 1 3 4a1 1 0 0 1 1-1h3.5a1 1 0 0 1 1 1c0 1.25.2 2.45.57 3.6a1 1 0 0 1-.25 1z"/>
          </svg>
        </span>
        <span>0412758391</span>
      </li>
    </ul>
    <div class="back-brand">RIDGELINE</div>
  </section>
</main>
</body>
</html>
```